Merriwick Law - New Letterhead/Logo

Hello!
THE FIRM NAME IS NOW MERRIWICK LAW. We recently just changed our name and we are in need of a classy letterhead. Attached I have a logo we have included in the past, but we are willing to look at other alternatives as well. I will also attach our current letterhead with our old name, Merriwick Law. We are willing to go without attorney names. Please help! Thanks

```html
<!DOCTYPE html>
<html lang="en">
<head>
<meta charset="utf-8">
<title>Merriwick Law Letterhead</title>
<link href="https://fonts.googleapis.com/css2?family=Nunito+Sans:wght@400;600&display=swap" rel="stylesheet">
<style>
  :root {
    --brand-blue: #3b63bc;
    --swoosh: #e6eef4;
    --ink: #111;
    --white: #fff;
    --backdrop: #f4f4f4;
  }
  html, body { margin: 0; padding: 0; width: 1200px; height: 1200px; overflow: hidden; background: var(--backdrop); }
  .letterhead {
    position: absolute; left: 158px; top: 27px;
    width: 885px; height: 1146px;
    background: var(--white);
    box-shadow: 0 8px 30px rgba(0,0,0,.18);
    font-family: "Nunito Sans", sans-serif;
    color: var(--ink);
    overflow: hidden;
  }
  .header-band { position: absolute; left: 0; top: 0; }
  .firm-name {
    position: absolute; right: 28px; top: 38px;
    color: var(--white); font-size: 23px; font-weight: 400; letter-spacing: .6px;
    padding-left: 12px; border-left: 2px solid var(--white); line-height: 48px;
  }
  .letter-body {
    position: absolute; left: 94px; top: 238px; width: 722px;
    font-size: 14px; line-height: 16.3px; letter-spacing: .05px;
  }
  .letter-body p { margin: 0 0 16px; }
  .closing { position: absolute; left: 139px; top: 879px; font-size: 17px; }
  .signature {
    position: absolute; left: 162px; top: 908px; width: 126px; height: 60px;
    background: linear-gradient(90deg, #ececec, #f6f6f6); border-radius: 4px;
  }
  .footer-band {
    position: absolute; left: 0; top: 1025px; width: 885px; height: 121px;
    background: var(--brand-blue); color: var(--white);
  }
  .footer-mark {
    position: absolute; left: 36px; top: 24px; width: 70px; height: 70px;
    border-radius: 50%; background: #6f92d6; border: 2px solid #a9c0ec;
  }
  .contact { position: absolute; display: flex; gap: 6px; align-items: flex-start; font-size: 12px; line-height: 16px; }
  .contact svg { flex: none; }
  .contact.phone { left: 441px; top: 9px; font-size: 16px; line-height: 17px; }
  .contact.address { left: 640px; top: 12px; font-size: 13px; }
  .contact.web { left: 441px; top: 67px; }
  .contact.mail { left: 642px; top: 67px; }
</style>
</head>
<body>
<div class="letterhead">
  <svg class="header-band" width="885" height="140" viewBox="0 0 885 140">
    <path d="M0 0H885V124C760 138 620 135 470 118C330 102 190 82 120 82C60 82 20 100 0 112Z" fill="var(--brand-blue)"/>
    <path d="M0 96C60 70 160 58 250 66C320 72 380 88 425 102C350 88 250 80 170 84C90 88 30 102 0 112Z" fill="var(--swoosh)"/>
  </svg>
  <div class="firm-name">Merriwick Law</div>

  <div class="letter-body">
    <p>Lorem ipsum dolor sit amet, consectetuer adipiscing elit. Nam cursus. Morbi ut mi. Nullam enim leo, egestas id, condimentum at, laoreet mattis, massa. Sed eleifend nonummy diam. Praesent mauris ante, elementum et, bibendum at, posuere sit amet, nibh. Duis tincidunt lectus quis dui viverra vestibulum. Suspendisse vulputate aliquam dui. Nulla elementum dui ut augue. Aliquam vehicula mi at mauris. Maecenas placerat, nisl at consequat rhoncus, sem nunc gravida justo, quis eleifend arcu velit quis lacus. Morbi magna magna, tincidunt a, mattis non, imperdiet vitae, tellus. Sed odio est, auctor ac, sollicitudin in, consequat vitae, orci. Fusce id felis. Vivamus sollicitudin.</p>
    <p>Metus eget eros. Pellentesque habitant morbi tristique senectus et netus et malesuada fames ac turpis egestas. In posuere felis nec tortor. Pellentesque faucibus. Ut accumsan ultricies elit. Maecenas at justo id velit placerat molestie. Donec dictum lectus non odio. Cras a ante vitae enim iaculis aliquam. Mauris nunc quam, venenatis nec, euismod sit amet, egestas placerat, est. Pellentesque habitant morbi tristique senectus et netus et malesuada fames ac turpis egestas. Cras id elit. Integer quis urna. Ut ante enim, dapibus malesuada, fringilla eu, condimentum quis, tellus. Aenean porttitor eros vel dolor. Donec convallis pede venenatis nibh. Duis quam. Nam eget.</p>
    <p>Lacus. Aliquam erat volutpat. Quisque dignissim congue leo. Mauris vel lacus vitae felis vestibulum volutpat. Etiam est nunc, venenatis in, tristique eu, imperdiet ac, nisl. Cum sociis natoque penatibus et magnis dis parturient montes, nascetur ridiculus mus. In iaculis facilisis massa. Etiam eu urna. Sed porta. Suspendisse quam leo, molestie sed, luctus quis, feugiat in, pede. Fusce tellus. Sed metus augue, convallis et, vehicula ut, pulvinar eu, ante. Integer orci tellus, tristique vitae, consequat nec, porta vel, lectus. Nulla sit amet diam. Duis non nunc. Nulla rhoncus dictum metus. Curabitur tristique mi condimentum orci. Phasellus pellentesque aliquam enim. Proin dui.</p>
    <p>Lectus, cursus eu, mattis laoreet, viverra sit amet, quam. Curabitur vel dolor ultrices ipsum dictum tristique. Praesent vitae lacus. Ut velit enim, vestibulum non, fermentum nec, hendrerit quis, leo. Pellentesque rutrum malesuada neque. Nunc tempus felis vitae urna. Vivamus porttitor, neque at volutpat rutrum, purus nisi eleifend libero, a tempus libero lectus feugiat felis. Morbi diam mauris, viverra in, gravida eu, mattis in, ante. Morbi eget arcu. Morbi porta, libero id ullamcorper nonummy, nibh ligula pulvinar metus, eget consectetuer augue nisi quis lacus. Ut ac mi quis lacus mollis aliquam. Curabitur iaculis tempus eros. Curabitur vel mi sit amet magna malesuada.</p>
    <p>Ultrices. Ut nisi erat, fermentum vel, congue id, euismod in, elit. Fusce ultricies, orci ac feugiat suscipit, leo massa sodales velit, et scelerisque mi tortor at ipsum. Proin orci odio, commodo ac, gravida non, tristique vel, tellus. Pellentesque nibh libero, ultricies eu, sagittis non, mollis sed, justo. Praesent metus ipsum, pulvinar pulvinar, porta id, fringilla at, est. Phasellus felis dolor, scelerisque a, tempus eget, lobortis id, libero. Donec scelerisque leo ac risus. Praesent sit amet est. In dictum, dolor eu dictum porttitor, enim felis viverra mi, eget luctus massa purus quis odio. Etiam nulla massa, pharetra facilisis, volutpat in, imperdiet.</p>
  </div>

  <div class="closing">sincerely</div>
  <div class="signature" role="img" aria-label="Handwritten signature of Merriwick"></div>

  <footer class="footer-band">
    <div class="footer-mark"></div>
    <div class="contact phone">
      <svg width="16" height="16" viewBox="0 0 16 16"><rect x="0.5" y="0.5" width="15" height="15" rx="3" fill="var(--white)"/><path d="M5 4c-1 1-1 3 1 5s4 3 5 2l-1-2-1.5.5c-1-.5-2-1.5-2.5-2.5L6.5 5.5Z" fill="var(--brand-blue)"/></svg>
      <div>(555)214 7380<br>(555)214 7381</div>
    </div>
    <div class="contact address">
      <svg width="22" height="22" viewBox="0 0 22 22"><circle cx="11" cy="11" r="10" fill="none" stroke="var(--white)" stroke-width="1.3"/><path d="M11 17s-4-4.2-4-7a4 4 0 0 1 8 0c0 2.8-4 7-4 7Z" fill="none" stroke="var(--white)" stroke-width="1.3"/><circle cx="11" cy="10" r="1.4" fill="var(--white)"/></svg>
      <div>1234<br>your adress</div>
    </div>
    <div class="contact web">
      <svg width="18" height="18" viewBox="0 0 18 18" fill="none" stroke="var(--white)" stroke-width="1.2"><circle cx="9" cy="9" r="8"/><ellipse cx="9" cy="9" rx="3.5" ry="8"/><path d="M1 9h16M2.5 5h13M2.5 13h13"/></svg>
      <div>www.merriwicklaw.com</div>
    </div>
    <div class="contact mail">
      <svg width="17" height="12" viewBox="0 0 17 12" fill="none" stroke="var(--white)" stroke-width="1.2"><rect x="0.6" y="0.6" width="15.8" height="10.8"/><path d="M.6.6 8.5 7l7.9-6.4M.6 11.4 6 5.5M16.4 11.4 11 5.5"/></svg>
      <div>office@merriwicklaw.com</div>
    </div>
  </footer>
</div>
</body>
</html>
```